Business Card Design Project

I need the following:

Logo -
Name - Dale Prewitt
Title - Customer Experience Officer
Web - www.bvrh.net
Phone - 555-417-3068
Updates

Project Deadline Extended
Reason: I launched the project later than anticipated. I look forward to seeing your designs. Dale

Industry/Entity Type

Business

```html
<!DOCTYPE html>
<html lang="en">
<head>
<meta charset="utf-8">
<title>Dale Prewitt – Business Card</title>
<link href="https://fonts.googleapis.com/css2?family=Archivo+Black&family=Montserrat:wght@300;800&display=swap" rel="stylesheet">
<style>
  :root {
    --page-bg: #2b2b2b;
    --card-bg: #ffffff;
    --card-edge: #e6e6e6;
    --ink: #1c1c1c;
    --brand-blue: #1b75bb;
    --brand-blue-light: #3d9ad8;
    --rule-dark: #2a2a2a;
    --muted: #3a3a3a;
  }
  * { box-sizing: border-box; margin: 0; padding: 0; }
  html, body {
    width: 1200px; height: 900px; overflow: hidden;
    background: var(--page-bg);
  }
  .card {
    position: absolute; left: 100px; top: 170px;
    width: 1000px; height: 560px;
    background: linear-gradient(160deg, var(--card-bg) 55%, #f0f0f0);
    border: 1px solid var(--card-edge);
    border-radius: 26px;
  }
  .brand {
    position: absolute; left: 70px; top: 50px;
    display: flex; align-items: center; gap: 34px;
  }
  .brand-mark {
    width: 150px; height: 150px; border-radius: 50%;
    background: var(--brand-blue);
  }
  .brand-name {
    font-family: "Archivo Black", sans-serif;
    color: var(--ink);
    font-size: 40px; line-height: 0.95;
    letter-spacing: 2px; text-transform: uppercase;
  }
  .brand-url {
    margin-top: 10px; padding-top: 4px;
    border-top: 2px solid var(--brand-blue-light);
    font-family: "Montserrat", sans-serif; font-weight: 800;
    font-size: 14px; color: var(--brand-blue);
    text-align: right; width: 300px;
  }
  .person {
    position: absolute; left: 70px; top: 270px; right: 60px;
  }
  .person-line {
    display: flex; align-items: center; gap: 20px;
  }
  .person-name {
    font-family: "Montserrat", sans-serif; font-weight: 800;
    font-size: 50px; color: var(--brand-blue);
    text-transform: uppercase; letter-spacing: 1px; white-space: nowrap;
  }
  .person-rule {
    flex: 1; height: 8px; background: var(--rule-dark);
  }
  .person-title {
    font-family: "Montserrat", sans-serif; font-weight: 300;
    font-size: 44px; color: var(--muted);
    text-transform: uppercase; letter-spacing: 4px; margin-top: 2px;
  }
  .contact {
    position: absolute; left: 70px; right: 60px; top: 440px;
    display: flex; justify-content: space-between; align-items: center;
  }
  .contact-item { display: flex; align-items: center; gap: 22px; }
  .contact-icon {
    width: 58px; height: 58px; border-radius: 50%;
    background: var(--brand-blue);
    display: flex; align-items: center; justify-content: center;
  }
  .contact-text {
    font-family: "Montserrat", sans-serif; font-weight: 800;
    font-size: 44px; color: var(--ink); letter-spacing: 1px;
  }
  .contact-text.web { font-size: 38px; }
</style>
</head>
<body>
  <main class="card">
    <div class="brand">
      <div class="brand-mark"></div>
      <div>
        <div class="brand-name">Bayview<br>Relay<br>Holdings</div>
        <div class="brand-url">www.bvrh.net</div>
      </div>
    </div>

    <div class="person">
      <div class="person-line">
        <span class="person-name">Dale Prewitt</span>
        <span class="person-rule"></span>
      </div>
      <div class="person-title">Customer Experience Officer</div>
    </div>

    <div class="contact">
      <div class="contact-item">
        <span class="contact-icon">
          <svg width="32" height="32" viewBox="0 0 24 24" fill="#fff" aria-hidden="true">
            <path d="M6.6 10.8c1.4 2.8 3.8 5.1 6.6 6.6l2.2-2.2c.3-.3.7-.4 1-.2 1.1.4 2.3.6 3.6.6.6 0 1 .4 1 1V20c0 .6-.4 1-1 1C10.6 21 3 13.4 3 4c0-.6.4-1 1-1h3.5c.6 0 1 .4 1 1 0 1.3.2 2.5.6 3.6.1.3 0 .7-.2 1l-2.3 2.2z"/>
          </svg>
        </span>
        <span class="contact-text">555-417-3068</span>
      </div>
      <div class="contact-item">
        <span class="contact-icon">
          <svg width="30" height="30" viewBox="0 0 24 24" fill="none" stroke="#fff" stroke-width="2.4" stroke-linecap="round" aria-hidden="true">
            <path d="M10 14a4 4 0 0 0 5.7 0l3-3a4 4 0 0 0-5.7-5.7l-1 1"/>
            <path d="M14 10a4 4 0 0 0-5.7 0l-3 3a4 4 0 0 0 5.7 5.7l1-1"/>
          </svg>
        </span>
        <span class="contact-text web">www.bvrh.net</span>
      </div>
    </div>
  </main>
</body>
</html>
```